Logo is done, need templates now

I want to be able to have an email template, same for word documents, powerpoint etc. I have the logo, now I need all the pieces for appearance in correspondence and marketing

Target Market(s)

Professional Advisors and Wealthy Clients

Font styles to use
Serif

Requirements
Must have
• I want to be able to do word documents and email them with letterhead. I need great email signatures. I need similar formatting for the word documents to be flexible to add to powerpoint and other presentations.

```html
<!DOCTYPE html>
<html lang="en">
<head>
<meta charset="utf-8">
<title>Stillwater Capital Letterhead</title>
<link href="https://fonts.googleapis.com/css2?family=Cormorant+Garamond:wght@500&family=Quicksand:wght@500;700&family=Arimo&display=swap" rel="stylesheet">
<style>
  :root {
    --canvas: #e7e4df;
    --paper: #f7f6ef;
    --teal: #2bbcc1;
    --teal-deep: #3aa5a3;
    --slate: #66767a;
    --ink: #2f3337;
    --white: #ffffff;
  }
  * { margin: 0; padding: 0; box-sizing: border-box; }
  html, body { width: 1200px; height: 900px; overflow: hidden; background: var(--canvas); }
  .canvas { position: relative; width: 1200px; height: 900px; }
  .letterhead {
    position: absolute; left: 267px; top: 20px; width: 666px; height: 860px;
    background: var(--paper); box-shadow: 0 4px 18px rgba(0,0,0,.12); overflow: hidden;
  }
  .letterhead__shapes { position: absolute; inset: 0; width: 666px; height: 860px; }
  .brand-name {
    position: absolute; left: 18px; right: 0; top: 92px; text-align: center;
    font-family: "Cormorant Garamond", serif; font-weight: 500; font-size: 21px;
    letter-spacing: .2em; color: var(--ink); text-transform: uppercase; white-space: nowrap;
  }
  .field {
    position: absolute; top: 183px; display: flex; align-items: flex-end; gap: 6px;
    font-family: "Arimo", sans-serif; font-size: 13px; color: var(--teal);
  }
  .field__line { display: block; height: 0; border-bottom: 2px solid var(--teal); margin-bottom: 2px; }
  .field--date { left: 82px; }
  .field--date .field__line { width: 127px; }
  .field--reference { left: 305px; }
  .field--reference .field__line { width: 204px; }
  .signature__name {
    position: absolute; left: 256px; top: 657px; white-space: nowrap;
    font-family: "Quicksand", sans-serif; font-weight: 700; font-size: 20px; color: var(--white);
  }
  .signature__role {
    position: absolute; left: 256px; top: 690px;
    font-family: "Quicksand", sans-serif; font-weight: 500; font-size: 13px; letter-spacing: .08em; color: var(--white);
  }
  .contact {
    position: absolute; left: 262px; display: flex; align-items: center; gap: 14px; white-space: nowrap;
    font-family: "Quicksand", sans-serif; font-weight: 700; font-size: 15px; letter-spacing: .1em; color: var(--white);
  }
  .contact__icon { width: 16px; height: 16px; flex: none; }
  .contact--phone { top: 728px; }
  .contact--email { top: 760px; }
  .contact--address { top: 792px; letter-spacing: .08em; }
  .signature__web {
    position: absolute; left: 248px; top: 827px; white-space: nowrap;
    font-family: "Quicksand", sans-serif; font-weight: 700; font-size: 15px; letter-spacing: .12em; color: var(--white);
  }
</style>
</head>
<body>
<div class="canvas">
  <div class="letterhead">
    <svg class="letterhead__shapes" viewBox="0 0 666 860">
      <defs>
        <linearGradient id="portrait-tone" x1="0" y1="0" x2="0" y2="1">
          <stop offset="0" stop-color="#e9eaea"/>
          <stop offset="1" stop-color="#4a4f54"/>
        </linearGradient>
      </defs>
      <rect class="edge-bar" x="0" y="0" width="18" height="860" fill="var(--teal)"/>
      <g class="footer-accents" fill="var(--teal)">
        <polygon points="140,644 160,644 145,663 125,663"/>
        <polygon points="170,644 195,644 180,663 155,663"/>
        <polygon points="205,644 225,644 210,663 190,663"/>
        <polygon points="52,752 60,752 40,780 32,780"/>
        <polygon points="30,780 38,780 52,794 44,794"/>
      </g>
      <polygon class="title-band" points="223,644 561,644 484,720 223,720" fill="var(--teal-deep)"/>
      <polygon class="contact-band" points="234,720 598,720 648,822 234,822" fill="var(--teal)"/>
      <polygon class="web-band" points="154,824 453,824 428,852 115,852" fill="var(--teal)"/>
      <rect class="portrait-shadow" x="52" y="670" width="182" height="170" fill="var(--slate)"/>
      <rect class="portrait-frame" x="45" y="663" width="180" height="170" fill="var(--teal)"/>
      <rect class="portrait" x="60" y="674" width="159" height="154" fill="url(#portrait-tone)" role="img" aria-label="Portrait photo of the director in a dark suit"/>
    </svg>

    <div class="brand-name">Stillwater Capital</div>

    <div class="field field--date"><span>Date:</span><span class="field__line"></span></div>
    <div class="field field--reference"><span>Reference:</span><span class="field__line"></span></div>

    <div class="signature__name">ANNA REID</div>
    <div class="signature__role">DIRECTOR</div>

    <div class="contact contact--phone">
      <svg class="contact__icon" viewBox="0 0 16 16"><path d="M3 1.5 L6 1 L7.5 4.5 L5.5 6 C6.5 8 8 9.5 10 10.5 L11.5 8.5 L15 10 L14.5 13 C14 14.5 12.5 15 11 14.5 C6.5 13 3 9.5 1.5 5 C1 3.5 1.5 2 3 1.5 Z" fill="var(--white)"/></svg>
      <span>1 555 204 718</span>
    </div>
    <div class="contact contact--email">
      <svg class="contact__icon" viewBox="0 0 16 16"><circle cx="8" cy="8" r="3" fill="none" stroke="var(--white)" stroke-width="1.8"/><path d="M11 5 V9.5 C11 11 13.5 11 14 9 C15 5 12 1.5 8 1.5 C4.5 1.5 1.5 4.5 1.5 8 C1.5 11.5 4.5 14.5 8 14.5 C9.5 14.5 10.5 14 11.5 13.5" fill="none" stroke="var(--white)" stroke-width="1.8"/></svg>
      <span>anna@stillwater.co</span>
    </div>
    <div class="contact contact--address">
      <svg class="contact__icon" viewBox="0 0 16 16"><path d="M8 15 C5 11 3 8.5 3 6 A5 5 0 0 1 13 6 C13 8.5 11 11 8 15 Z" fill="none" stroke="var(--white)" stroke-width="1.4"/><circle cx="8" cy="6" r="1.8" fill="none" stroke="var(--white)" stroke-width="1.4"/></svg>
      <span>Harbor Lane, Westfield Court.</span>
    </div>

    <div class="signature__web">www.stillwater.co</div>
  </div>
</div>
</body>
</html>
```